Willowbend Pharmacy Business Cards

I need a business card design and or template. Needs to convey a softer feel along with health and wellness. Please see attached logo and color scheme.

Industry/Entity Type

Pharmacy

Colors

Designer to choose colors to be used in the design.

Requirements
Must have
• I've added a second NEW colored logo I think I am going to go with the blue green logo.
• Needs to have the colors and feel of the logo attached.
• Darrel Quimby
• Pharmacy Manager
• willowbendpharmacy.example

```html
<!DOCTYPE html>
<html lang="en">
<head>
<meta charset="utf-8">
<title>Willowbend Pharmacy – Business Card</title>
<link rel="stylesheet" href="https://fonts.googleapis.com/css2?family=Arimo:wght@400;700&family=Noto+Sans:ital,wght@1,800&display=swap">
<style>
  :root {
    --page-bg: #ffffff;
    --card-top: #62b445;
    --card-mid: #3f9a3f;
    --card-bottom: #1a7138;
    --ink: #050505;
    --swoosh-grey: #6b6f72;
    --swoosh-pink: #e56f8e;
    --leaf-green: #a8cb4a;
  }
  html, body {
    margin: 0;
    padding: 0;
    width: 1200px;
    height: 852px;
    overflow: hidden;
    background: var(--page-bg);
  }
  .canvas {
    position: relative;
    width: 1200px;
    height: 852px;
  }
  .business-card {
    position: absolute;
    left: 37px;
    top: 160px;
    width: 1123px;
    height: 642px;
    overflow: hidden;
    background: linear-gradient(170deg, var(--card-top) 0%, var(--card-mid) 45%, var(--card-bottom) 100%);
  }
  .swoosh {
    position: absolute;
    left: 0;
    top: 0;
    width: 1123px;
    height: 642px;
  }
  .swoosh-grey { fill: var(--swoosh-grey); }
  .swoosh-pink { fill: var(--swoosh-pink); }
  .brand-name {
    position: absolute;
    left: 40px;
    top: 290px;
    width: 300px;
    margin: 0;
    font-family: "Arimo", Arial, sans-serif;
    font-weight: 700;
    font-size: 42px;
    line-height: 1.1;
    color: var(--swoosh-pink);
  }
  .holder-name {
    position: absolute;
    right: 48px;
    top: 12px;
    margin: 0;
    font-family: "Noto Sans", Verdana, sans-serif;
    font-style: italic;
    font-weight: 800;
    font-size: 72px;
    letter-spacing: 2px;
    line-height: 1;
    color: var(--ink);
    text-transform: uppercase;
    white-space: nowrap;
  }
  .holder-role {
    position: absolute;
    left: 546px;
    top: 98px;
    width: 420px;
    margin: 0;
    text-align: center;
    font-family: "Arimo", Arial, sans-serif;
    font-weight: 400;
    font-size: 38px;
    line-height: 1.2;
    color: var(--ink);
  }
  .website {
    position: absolute;
    right: 48px;
    bottom: 18px;
    margin: 0;
    font-family: "Arimo", Arial, sans-serif;
    font-weight: 400;
    font-size: 42px;
    line-height: 1.2;
    color: var(--leaf-green);
    white-space: nowrap;
  }
</style>
</head>
<body>
<main class="canvas">
  <section class="business-card">
    <svg class="swoosh" viewBox="0 0 1123 642" aria-hidden="true">
      <path class="swoosh-grey" d="M203,0 C330,90 440,250 433,400 C428,500 380,590 342,642 L487,642 C520,520 535,420 520,330 C490,190 330,60 215,0 Z"/>
      <path class="swoosh-pink" d="M215,0 C330,60 490,190 520,330 C535,420 520,520 487,642 L390,642 C435,540 470,450 465,380 C455,250 360,110 215,0 Z"/>
    </svg>
    <p class="brand-name">Willowbend<br>Pharmacy</p>
    <h1 class="holder-name">Darrel Quimby</h1>
    <p class="holder-role">Pharmacy Manager</p>
    <p class="website">willowbendpharmacy.example</p>
  </section>
</main>
</body>
</html>
```